Luminously Grounded Vitality

We want to design a business card that is modern and appealing for an innovative psychedelic telemedicine company that provides at-home ketamine-assisted therapy along with wellness, longevity, and anti-aging medicines. We want to use our deep purple and white plus other colors you can find on our website. We don't have any strict brand guidelines yet so feel free to get creative. We want a very professional, but technology first modern design that will instill trust, peace, calm, but also be attractive to investors in the healthcare and SaaS space.

```html
<!DOCTYPE html>
<html lang="en">
<head>
<meta charset="utf-8">
<title>Luminously Grounded Vitality – Business Card</title>
<link rel="stylesheet" href="https://fonts.googleapis.com/css2?family=Questrial&display=swap">
<style>
  :root {
    --bg: #e4e5e8;
    --card: #ffffff;
    --purple: #7a66b3;
    --orchid: #c475c1;
    --brand: #a7559f;
    --ink: #4a4a4f;
    --rule: #d6d6dc;
  }
  * { box-sizing: border-box; margin: 0; padding: 0; }
  html, body { width: 1200px; height: 800px; overflow: hidden; }
  body {
    background: var(--bg);
    font-family: "Questrial", "Century Gothic", sans-serif;
    color: var(--ink);
    display: flex;
    align-items: center;
    justify-content: center;
    gap: 50px;
  }
  .card {
    position: relative;
    width: 540px;
    height: 309px;
    background: var(--card);
    box-shadow: 0 6px 18px rgba(0,0,0,0.12);
    overflow: hidden;
  }
  .card-band {
    position: absolute;
    left: 0; right: 0;
    bottom: 22px;
    height: 14px;
    background: linear-gradient(90deg, var(--orchid), var(--purple));
  }
  .wordmark {
    display: flex;
    align-items: center;
    gap: 12px;
    color: var(--brand);
    font-size: 38px;
    letter-spacing: 0.5px;
  }
  .wordmark-dot {
    width: 34px; height: 34px;
    border-radius: 50%;
    background: var(--purple);
  }

  /* Back side */
  .card-back .wordmark {
    position: absolute;
    left: 50%; top: 112px;
    transform: translateX(-50%);
  }

  /* Front side */
  .card-front .wordmark {
    position: absolute;
    right: 36px; top: 36px;
  }
  .rule {
    position: absolute;
    left: 32px; right: 32px;
    height: 1px;
    background: var(--rule);
  }
  .rule-top { top: 112px; }
  .rule-mid { top: 196px; left: 250px; }
  .person {
    position: absolute;
    right: 36px; top: 124px;
    text-align: right;
  }
  .person-name {
    color: var(--brand);
    font-size: 14px;
    font-weight: 700;
    letter-spacing: 0.6px;
  }
  .person-title { font-size: 13px; margin-top: 3px; }
  .contact {
    position: absolute;
    left: 34px; top: 124px;
    list-style: none;
    font-size: 13px;
    line-height: 21px;
  }
  .contact li { display: flex; align-items: center; gap: 8px; }
  .contact svg { width: 12px; height: 12px; fill: var(--brand); flex: none; }
  .address {
    position: absolute;
    right: 36px; top: 206px;
    text-align: right;
    font-size: 13px;
    line-height: 18px;
  }
</style>
</head>
<body>
  <section class="card card-back" aria-label="Card back">
    <div class="wordmark"><span class="wordmark-dot"></span>Luminously</div>
    <div class="card-band"></div>
  </section>

  <section class="card card-front" aria-label="Card front">
    <div class="wordmark"><span class="wordmark-dot"></span>Luminously</div>
    <div class="rule rule-top"></div>

    <ul class="contact">
      <li>
        <svg viewBox="0 0 24 24" aria-hidden="true"><path d="M6.6 10.8a15 15 0 0 0 6.6 6.6l2.2-2.2a1 1 0 0 1 1-.25 11.4 11.4 0 0 0 3.6.57 1 1 0 0 1 1 1V20a1 1 0 0 1-1 1A17 17 0 0 1 3 4a1 1 0 0 1 1-1h3.5a1 1 0 0 1 1 1c0 1.25.2 2.45.57 3.6a1 1 0 0 1-.25 1z"/></svg>
        833-555-0147
      </li>
      <li>
        <svg viewBox="0 0 24 24" aria-hidden="true"><path d="M3 5h18v14H3zm2 2v.5l7 5 7-5V7l-7 5z"/></svg>
        hello@luminously.com
      </li>
      <li>
        <svg viewBox="0 0 24 24" aria-hidden="true"><path d="M12 2a10 10 0 1 0 0 20 10 10 0 0 0 0-20zm0 2a8 8 0 0 1 0 16 8 8 0 0 1 0-16zm-1 3v5.4l4.3 2.6 1-1.6-3.3-2V7z"/></svg>
        www.luminously.com
      </li>
    </ul>

    <div class="person">
      <div class="person-name">MAREN ELLISON, FNP-C</div>
      <div class="person-title">Co-founder, Chief Clinical Officer</div>
    </div>

    <div class="rule rule-mid"></div>

    <address class="address" style="font-style:normal">
      245 Larkspur Avenue<br>
      Suite 900 Boulder, CO<br>
      United States, Colorado
    </address>

    <div class="card-band"></div>
  </section>
</body>
</html>
```